Fashion-Doll Website

I'm looking to create a new and better website for my growing fashion-doll brand, MARLOW.

About me: I'm a Brooklyn-based artist, illustrator, and doll-maker and MARLOW is the name of my doll. Marlow is a character doll (one girl) but she's not necessarily defined by any particular physical trait outside of the sculpt of the doll and her unique sense of style. For example, she could have pink hair and freckles or dark skin and green eyes, but she would still be "Marlow."

My partner and I created the current website ourselves using Adobe Muse. While it has served its purpose, we are not professional graphic or web designers, so I'm looking to graduate to a much more sophisticated and streamlined web design. I want the site to feel sweet and homespun but also hip and edgy. Because the site is so image heavy, I think black and white or black and off-white might be the best color palate, but I'm open to seeing other palates. Marlow's signature color is a muted lavender so maybe that could be integrated into the design. Here is the link:

www.MarlowFigure.com

I want the website to feel more like a shop and less like a gallery/info page. I'm now selling one-of-a-kind porcelain dolls, limited-edition resin dolls, face-plate necklaces, paper dolls, custom doll services, and printed Marlow throw pillows. I also need an interface that will allow me to create new categories, update inventory, and post new items easily.

I need to add new sections for press/articles, multiple image galleries (photography, products, illustrations, comics, and fan art), **collaboration projects, and several flash based doll "dress-up" games.

I would prefer a design that I can code/update myself using Adobe Muse. PSD files import into Muse, so I would prefer that you use them. I'm certainly not opposed to other designs, but I would prefer a design I can manage myself.

I'm including some photos and drawings of Marlow that express her look and vibe. I don't want to use these images in the web design necessarily (I think simple is best) but I thought they would be helpful in expressing the kind of girl she is and how I want the site to feel. I want to work with someone who has a clean, refined, yet whimsical aesthetic who can help me create a website that really expresses how special Marlow is.

Reason: I have had a family emergency come up and I can't devote time to this right now so I'm extending the deadline another 10 days.

Target Market(s)

young eccentrics, art collectors, fashion enthusiasts, and adult doll-collectors

Industry/Entity Type

Fashion

Requirements
Must have
• I need the following main categories: Info, Sales, Galleries, Press, and Dress-up. However, I don't necessarily want or expect the layout to be organized like the current website.

INFO:

*About Marlow (the character)

*Doll specifications: 27" porcelain doll, 22" porcelain doll, 22" resin doll, life-size doll (for window display)

*About the artist

SALES:

*Porcelain dolls

*Resin dolls

*Face-plate necklaces

*Pillows

*Custom doll/necklace info and inquiry form

GALLERIES:

*Photographs

*Collaboration projects

*Illustrations/Comics

*Fan Art/Contests

PRESS:

*An inventory of pdf's of articles about Marlow for users to download or view inside a reader online.

DRESS UP:

*Links to two interactive flash based dress-up games (interactive paper dolls)

Nice to have
• I hold online drawing and design contests from time to time so I would love to have a spot on the site reserved to host the rules and results of my contests.

Marlow has a large facebook and Instagram following so links to her social media would also be great.
instagram: @marlowfigure
facebook: facebook.com/marlowfigure

Should not have
• I'm not looking to see anything too girly, too young, or too sexy.
Marlow is not Tessa, Meadow Child, or Zoomi. She's a sophisticated young girl who is fresh, funky, and free-spirited.

```html
<!DOCTYPE html>
<html lang="en">
<head>
<meta charset="utf-8">
<title>Marlow Doll</title>
<link href="https://fonts.googleapis.com/css2?family=Source+Sans+3:wght@300;400;600&display=swap" rel="stylesheet">
<style>
  :root{
    --pink:#f2539f;
    --pink-light:#ff86bf;
    --pink-dark:#e9479a;
    --ink:#222222;
    --text:#555555;
    --muted:#777777;
    --band:#f1f1f1;
    --footer:#202020;
    --lime-top:#d6ea6a;
    --lime-bottom:#a9c934;
    --white:#ffffff;
  }
  *{box-sizing:border-box;margin:0;padding:0}
  html,body{width:1194px;height:1200px;overflow:hidden;background:var(--white)}
  body{position:relative;font-family:"Source Sans 3",Arial,sans-serif;color:var(--text)}
  .abs{position:absolute}

  /* header */
  .brand{left:84px;top:30px;font-size:68px;font-weight:300;letter-spacing:4px;color:var(--ink);line-height:1}
  .social-top{left:1040px;top:46px;display:flex;gap:9px}
  .social-top span{width:26px;height:26px;border-radius:3px;display:block}
  .sq-blue{background:#3b66b0}
  .sq-brown{background:#7a5a3c}
  .sq-sky{background:#3fa9e6}
  .sq-navy{background:#2f78b8}
  .search{left:826px;top:84px;width:285px;height:35px;border:2px solid #dcdcdc;border-radius:18px;background:#fff;font-size:14px;font-style:italic;color:#999;padding:7px 16px}
  .search svg{position:absolute;right:13px;top:7px}

  /* nav */
  .nav{left:79px;top:136px;width:1036px;height:55px;background:linear-gradient(#ff8ac2,var(--pink-dark));border-radius:3px 3px 0 0;display:flex}
  .nav a{color:#fff;text-decoration:none;font-size:23px;font-weight:300;line-height:55px;text-align:center;border-right:1px solid #c73a80;box-shadow:1px 0 0 #ff9fcd}
  /* hero */
  .hero-band{left:0;top:191px;width:1194px;height:419px;background:var(--band)}
  .hero-panel{left:79px;top:191px}
  .hero-kicker{left:144px;top:244px;font-size:35px;font-weight:300;color:#666}
  .hero-title{left:144px;top:280px;font-size:45px;font-weight:400;color:#333}
  .hero-text{left:146px;top:334px;width:390px;font-size:13.5px;line-height:22px;font-weight:300;color:#666}
  .btn-grey{left:146px;top:391px;width:113px;height:34px;border-radius:3px;background:linear-gradient(#fafafa,#dedede);box-shadow:0 1px 2px rgba(0,0,0,.3);font-size:14px;color:#555;text-align:center;line-height:34px}
  .slider-dot{left:145px;top:450px;width:41px;height:41px;border-radius:50%;background:var(--pink)}
  .hero-photo{left:580px;top:198px;width:470px;height:365px;border-radius:40% 40% 8px 8px;background:linear-gradient(120deg,#b8a6c8 0%,#e9e2dc 40%,#c84a3c 70%,#3f5a3a 100%);opacity:.85}

  /* content */
  .welcome-title{left:79px;top:662px;font-size:28px;font-weight:400;color:var(--ink)}
  .welcome-sub{left:81px;top:707px;width:320px;font-size:19px;line-height:24px;font-weight:300;color:#555}
  .welcome-body{left:81px;top:763px;width:390px;font-size:13.6px;line-height:24.5px;font-weight:300;color:#666}
  .welcome-body p+p{margin-top:9px}
  .btn-lime{left:81px;top:934px;width:107px;height:36px;border-radius:3px;background:linear-gradient(var(--lime-top),var(--lime-bottom));border:1px solid #9bb72d;font-size:13px;color:#3d4a10;text-align:center;line-height:34px}

  .col-title{font-size:24px;font-weight:300;color:var(--pink)}
  .contest-title{left:504px;top:664px}
  .contest-card{left:506px;top:705px}
  .contest-art{left:521px;top:719px;width:250px;height:163px;border-radius:6px;background:linear-gradient(135deg,#f2efe8,#c8c07a 45%,#9aa4ba 75%,#ece9e4)}
  .contest-name{left:526px;top:888px;font-size:24px;font-weight:400;color:#fff}
  .contest-text{left:527px;top:920px;width:240px;font-size:12.5px;line-height:18px;font-weight:300;color:#fff}

  .winners-title{left:822px;top:664px}
  .thumbs{left:826px;top:706px;display:grid;grid-template-columns:repeat(3,86px);grid-gap:7px 13px}
  .thumb{height:76px;border:2px solid #fff;box-shadow:0 0 0 1px #ddd;border-radius:3px}
  .t1{background:linear-gradient(#e8c48a,#e9a57e)}
  .t2{background:linear-gradient(#e5e1dc,#c9c3bb)}
  .t3{background:linear-gradient(#4a3b3a,#e9cdc4)}
  .t4{background:linear-gradient(#f0ece6,#d8cdbd)}
  .t5{background:linear-gradient(#c4503c,#8a4a36)}
  .t6{background:linear-gradient(#9f8ab0,#d7c8cf)}
  .winner-name{left:825px;top:877px;font-size:21px;font-weight:400;color:#555}
  .winner-text{left:826px;top:906px;width:290px;font-size:12.5px;line-height:18px;font-weight:300;color:#888}

  /* footer */
  .footer{left:0;top:1068px;width:1194px;height:132px;background:var(--footer)}
  .footer-links{left:88px;top:1103px;font-size:17.5px;color:#fff;font-weight:400}
  .footer-links a{color:#fff;text-decoration:none}
  .footer-links i{font-style:normal;margin:0 7px}
  .copyright{left:87px;top:1138px;font-size:13px;font-weight:300;color:#bbb}
  .social-foot{left:1038px;top:1105px;display:flex;gap:5px}
  .social-foot span{width:22px;height:22px;border-radius:3px;display:block}
</style>
</head>
<body>

<header>
  <div class="abs brand">MARLOW</div>
  <div class="abs social-top" aria-label="Social links">
    <span class="sq-blue"></span>
    <span class="sq-brown"></span>
  </div>
  <div class="abs search">Search here..
    <svg width="18" height="18" viewBox="0 0 18 18"><circle cx="7.5" cy="7.5" r="5.5" fill="none" stroke="#888" stroke-width="2.5"/><line x1="11.5" y1="11.5" x2="16" y2="16" stroke="#888" stroke-width="3" stroke-linecap="round"/></svg>
  </div>
  <nav class="abs nav">
    <a href="#" style="width:129px">Home</a>
    <a href="#" style="width:103px">Info</a>
    <a href="#" style="width:110px">Sales</a>
    <a href="#" style="width:148px">Galleries</a>
    <a href="#" style="width:118px">Press</a>
    <a href="#" style="width:143px">Dress Up</a>
  </nav>
</header>

<section>
  <div class="abs hero-band"></div>
  <svg class="abs hero-panel" width="1036" height="400" viewBox="0 0 1036 400">
    <defs>
      <filter id="soft" x="-5%" y="-20%" width="110%" height="160%"><feGaussianBlur stdDeviation="6"/></filter>
    </defs>
    <path d="M20 345 Q518 400 1016 345 L1016 362 Q518 398 20 362Z" fill="#999" opacity=".55" filter="url(#soft)"/>
    <path d="M0 0 H1036 V340 Q1036 348 1026 350 Q518 410 10 350 Q0 348 0 340Z" fill="#fff"/>
  </svg>
  <div class="abs hero-photo" role="img" aria-label="Three Marlow dolls in green, polka-dot and coral dresses"></div>
  <div class="abs hero-kicker">Class aptent taciti</div>
  <div class="abs hero-title">Duis sed tellus et tortor</div>
  <p class="abs hero-text">Mauris vel lacus vitae felis vestibulum volutpat. Etiam est nunc, venenatis in, tristique eu, imperdiet ac, nisl.</p>
  <div class="abs btn-grey">LEARN MORE</div>
  <div class="abs slider-dot">
    <svg width="41" height="41" viewBox="0 0 41 41"><path d="M18 14 L12 20.5 L18 27 M23 14 L29 20.5 L23 27" fill="none" stroke="#fff" stroke-width="2"/></svg>
  </div>
</section>

<main>
  <h1 class="abs welcome-title" style="font-weight:400">Welcome to Marlow Doll Mainpage</h1>
  <p class="abs welcome-sub">Mauris neque metus, malesuada nec ultricies sit amet, porttitor</p>
  <div class="abs welcome-body">
    <p>Marlow is a modern take on the classic European fashion doll. Each element of Marlow is designed and handcrafted, from the heirloom-quality porcelain to the custom wigs and garments.</p>
    <p>Her look embodies Brooklyn street-style, Manhattan sophistication, and the classic lines of yesterday.&nbsp; Marlow represents a new chapter in the venerable tradition of boutique doll-making.</p>
  </div>
  <div class="abs btn-lime">LEARN MORE</div>

  <h2 class="abs col-title contest-title">Drawing/ Design Contests</h2>
  <svg class="abs contest-card" width="276" height="278" viewBox="0 0 276 278">
    <path d="M3 0 H273 Q276 0 276 3 V260 Q200 256 130 266 Q60 278 3 268 Q0 268 0 264 V3 Q0 0 3 0Z" fill="var(--pink)"/>
  </svg>
  <div class="abs contest-art" role="img" aria-label="Contest illustration of a girl lounging with cushions and a cat"></div>
  <div class="abs contest-name">Drawing Contest Name</div>
  <p class="abs contest-text">Proin nulla arcu, nonummy luctus&nbsp; dic tum eget fermentum</p>

  <h2 class="abs col-title winners-title">This Month Winners</h2>
  <div class="abs thumbs">
    <div class="thumb t1" role="img" aria-label="Winning doll portrait with flower crown"></div>
    <div class="thumb t2" role="img" aria-label="Winning drawing of a doll with red roses"></div>
    <div class="thumb t3" role="img" aria-label="Winning doll portrait in soft pink"></div>
    <div class="thumb t4" role="img" aria-label="Winning doll portrait with pale hair"></div>
    <div class="thumb t5" role="img" aria-label="Winning doll portrait with red hair"></div>
    <div class="thumb t6" role="img" aria-label="Winning doll portrait with lavender hair"></div>
  </div>
  <div class="abs winner-name">Class aptent taciti sociosqu</div>
  <p class="abs winner-text">Aliquam nec erat at purus cursus interdum. Vestibu-lum ligula augue, bibendum accumsan</p>
</main>

<footer>
  <div class="abs footer"></div>
  <div class="abs footer-links"><a href="#">Home</a><i>|</i><a href="#">Info</a><i>|</i><a href="#">Sales</a><i>|</i><a href="#">Galleries</a><i>|</i><a href="#">Press</a><i>|</i><a href="#">Dress Up</a></div>
  <div class="abs copyright">Copyright ©&nbsp; 2013 Company Name. All rights reserved.</div>
  <div class="abs social-foot" aria-label="Social links">
    <span class="sq-sky"></span>
    <span class="sq-navy"></span>
    <span class="sq-blue"></span>
  </div>
</footer>

</body>
</html>
```